Neuroepigenetics Symposium Save the Date

We need a Save the Date flyer for our upcoming Neuroepigenetics Symposium. This flyer should include the following:

Speakers, which we have eleven speakers with two name lecture speakers for this event.

1. Korvath Lecture:
Mira Talvessen, M.D.
Professor in the departments of Pediatrics, Molecular and Human Genetics, and Neurology and Neuroscience at Wrenfield College of Medicine, the director of the Tess and Owen Marlow Neurological Research Institute at Brightvale Children’s Hospital, and an investigator of the Calder Finch Medical Institute.
2. Linwood Lecture:
Tobias Renquist, Ph.D.
Elias Ward Cotter Professor of Neurobiology at Kestrel Medical School
3. R. Martin Olvey, Ph.D.
Professor and Chairman, Department of Pharmacology at Ashcombe University.
4. Teodor Haskel, M.D., Ph.D.
Fairholt Professor and Chair of Neuroscience at Pellridge University St. Louis
5. Clara Vintner, Ph.D.
Associate Professor of Neuroscience and Psychiatry at Oberlay School of Medicine at Mount Carrow
6. Pavel Strondeka, Ph.D.
Associate Professor of Pathology, Neurology & Neuroscience at Halvern University
7. Xiumei Tang, Ph.D.
Associate Professor of Genetics at the Whitacre School of Medicine at the University of Marrowdale
8. Katrina Moss, Ph.D.
Assistant Professor of Pharmacology at the Whitacre School of Medicine at the University of Marrowdale
9. Lorenzo Vetrani, Ph.D.
Assistant Professor of Cell and Developmental Biology at the Whitacre School of Medicine at the University of Marrowdale
10. Alison Garrow-Tenley, Ph.D.
Assistant Professor of Bioengineering at the Quillan School of Engineering and Applied Science at the University of Marrowdale
11. Helen Varsky, Ph.D.
Agnes T.W. Holloway Professor of Biology; Investigator of the Calder Finch Medical Institute at the Brookline School of Arts and Sciences at the University of Marrowdale.
***Please shorten if necessary.

Date/Time, this event will take place on January 9th, 2017 from 8:30am - 6pm with reception from 5-6pm, and on January 10th, 2017 from 8:30am - 12pm.

Location, is Orrin Center for Translational Research, Castellan Auditorium and Lobby, 2750 Harbor Point Blvd, Philadelphia, PA 19187.

Title of event, KORT 33rd Annual Symposium "Year of Neuroepigenetics". This symposium is a joint collaboration sponsors by the Marrowdale Epigenetics Program, and Kessler Institute for Neurosciences (KORT). (department logos attached)

Outside sponsor, Veltrosyn's logo can be really small on the flyer. (logo attached)

I hope to include pictures of the speakers, but I am still waiting for them to send me the images they would like me to use. So, please work with this for now.

```html
<!DOCTYPE html>
<html lang="en">
<head>
<meta charset="utf-8">
<title>KORT 33rd Annual Symposium – Year of Neuroepigenetics</title>
<link rel="stylesheet" href="https://fonts.googleapis.com/css2?family=Arimo:ital,wght@0,400;0,700;1,400;1,700&display=swap">
<style>
  :root {
    --bg-top: #47575d;
    --bg-mid: #33424a;
    --bg-bottom: #1d262a;
    --helix-light: #8fa2aa;
    --helix-dark: #27343a;
    --text: #ffffff;
    --text-soft: #e4eaec;
    --rule: rgba(255,255,255,0.55);
    --panel: rgba(255,255,255,0.06);
  }
  * { margin: 0; padding: 0; box-sizing: border-box; }
  html, body { width: 857px; height: 1200px; overflow: hidden; }
  body {
    font-family: "Arimo", Arial, sans-serif;
    color: var(--text);
    background: radial-gradient(ellipse at 55% 20%, var(--bg-top) 0%, var(--bg-mid) 45%, var(--bg-bottom) 100%);
    position: relative;
  }
  .helix-art {
    position: absolute; left: 0; top: 0; width: 430px; height: 1200px;
    background: linear-gradient(100deg, rgba(39,52,58,0) 0%, rgba(143,162,170,0.28) 35%, rgba(143,162,170,0.12) 60%, rgba(39,52,58,0) 100%);
  }
  .masthead { position: absolute; left: 205px; top: 42px; }
  .brand-mark { position: absolute; left: 0; top: 2px; width: 84px; height: 84px; background: var(--text); }
  .title-block { position: absolute; left: 95px; top: 0; width: 540px; }
  .title-block h1 { font-size: 41px; font-weight: 700; line-height: 41px; letter-spacing: 0.5px; }
  .title-block .edition { font-size: 41px; font-weight: 400; line-height: 43px; }
  .title-block .edition sup { font-size: 24px; }
  .title-block .theme { font-size: 41px; font-weight: 700; line-height: 44px; }

  .event-details { position: absolute; left: 300px; top: 192px; width: 540px; font-size: 19px; line-height: 23px; }
  .event-details strong { font-weight: 700; }
  .event-details .dates { margin-bottom: 14px; }

  .lectures {
    position: absolute; left: 428px; top: 372px; width: 400px; height: 108px;
    background: var(--panel);
    border-bottom: 1px solid var(--rule);
    display: flex;
  }
  .lecture { width: 50%; padding: 10px 0 0 12px; }
  .lecture .label { font-size: 17px; line-height: 20px; }
  .lecture .name { font-size: 19px; font-weight: 700; line-height: 23px; }
  .lecture .role { font-size: 11px; font-style: italic; line-height: 13px; color: var(--text-soft); }

  .speakers { position: absolute; left: 430px; top: 497px; width: 400px; text-align: center; list-style: none; }
  .speakers li { height: 61px; }
  .speakers .name { font-size: 20px; font-weight: 700; line-height: 24px; }
  .speakers .role { font-size: 13px; font-style: italic; line-height: 16px; color: var(--text-soft); }

  .partners { position: absolute; left: 470px; top: 1058px; width: 360px; display: flex; justify-content: space-between; font-size: 13px; font-style: italic; }
  .partner { text-align: center; width: 170px; }
  .partner .mark-row { margin-top: 8px; display: flex; align-items: center; justify-content: center; gap: 6px; font-style: normal; font-size: 12px; font-weight: 700; }
  .partner .circle { width: 48px; height: 48px; border-radius: 50%; background: var(--text); flex: none; }
  .partner .square { width: 16px; height: 16px; background: var(--text); flex: none; }
  .partner .mark-row.stack { flex-direction: column; gap: 4px; }
</style>
</head>
<body>
  <div class="helix-art" role="img" aria-label="Glossy double helix DNA strand running down the left side"></div>

  <header class="masthead">
    <div class="brand-mark" aria-hidden="true"></div>
    <div class="title-block">
      <h1>KORT</h1>
      <p class="edition">33<sup>rd</sup> Annual Symposium</p>
      <p class="theme">"Year of Neuroepigenetics"</p>
    </div>
  </header>

  <section class="event-details">
    <p class="dates"><strong>on January 9th, 2017</strong> from 8:30am - 6pm<br>with reception from 5-6pm, and<br><strong>on January 10th, 2017</strong> from 8:30am - 12pm.</p>
    <p class="venue">at <strong>Orrin Center for Translational Research</strong>,<br>Castellan Auditorium and Lobby,<br>2750 Harbor Point Blvd, Philadelphia, PA 19187.</p>
  </section>

  <section class="lectures">
    <div class="lecture">
      <p class="label">Korvath Lecture:</p>
      <p class="name">Mira Talvessen, M.D.</p>
      <p class="role">Professor in the departments of Pediatrics, Molecular and Human Genetics, and Neurology and Neuroscience</p>
    </div>
    <div class="lecture">
      <p class="label">Linwood Lecture:</p>
      <p class="name">Tobias Renquist, Ph.D.</p>
      <p class="role">Elias Ward Cotter Professor of Neurobiology</p>
    </div>
  </section>

  <ul class="speakers">
    <li><p class="name">R. Martin Olvey, Ph.D</p><p class="role">Professor and Chairman, Department of Pharmacology</p></li>
    <li><p class="name">Teodor Haskel, M.D., Ph.D.</p><p class="role">Fairholt Professor and Chair of Neuroscience</p></li>
    <li><p class="name">Clara Vintner, Ph.D.</p><p class="role">Associate Professor of Neuroscience and Psychiatry</p></li>
    <li><p class="name">Pavel Strondeka, Ph.D.</p><p class="role">Associate Professor of Pathology, Neurology &amp; Neuroscience</p></li>
    <li><p class="name">Xiumei Tang, Ph.D.</p><p class="role">Associate Professor of Genetics at the Whitacre School of Medicine</p></li>
    <li><p class="name">Katrina Moss, Ph.D.</p><p class="role">Assistant Professor of Pharmacology at the Whitacre School of Medicine</p></li>
    <li><p class="name">Lorenzo Vetrani, Ph.D.</p><p class="role">Assistant Professor of Cell and Developmental Biology</p></li>
    <li><p class="name">Alison Garrow-Tenley, Ph.D.</p><p class="role">Assistant Professor of Bioengineering</p></li>
    <li><p class="name">Helen Varsky, Ph.D.</p><p class="role">Agnes T.W. Holloway Professor of Biology; Investigator of the Calder Finch<br>Medical Institute</p></li>
  </ul>

  <footer class="partners">
    <div class="partner">
      <p>In collaboration with</p>
      <div class="mark-row stack"><span class="circle"></span><span>Marrowdale Epigenetics Program</span></div>
    </div>
    <div class="partner">
      <p>Sponsor</p>
      <div class="mark-row"><span class="square"></span><span>Veltrosyn</span></div>
    </div>
  </footer>
</body>
</html>
```